Modern wordpress-enabled design wanted for translations agency serving large corporations

We are a translation agency and we only work for corporate clients and not private individuals. We are currently using the Larvesk wordpress theme and an upload feature called trobanex. It is important that prospective clients can upload their file. So we need a cool design for that kind of feature. We offer different kinds of translations tailored to the needs or global corporations. Corporate communications translations, legal translations, financial translations, healthcare translations, financial translations, audit translations.

```html
<!DOCTYPE html>
<html lang="en">
<head>
<meta charset="utf-8">
<title>Verbalis Translation</title>
<link href="https://fonts.googleapis.com/css2?family=Raleway:wght@400;500;600&family=Open+Sans:wght@400;600&display=swap" rel="stylesheet">
<style>
:root{
  --green:#4a9a2a;
  --green-dark:#3c8520;
  --blue:#1f3fa8;
  --ink:#333;
  --muted:#8a8a8a;
  --line:#e3e3e3;
  --dark:#1e1e1e;
  --darker:#141414;
  --white:#fff;
}
*{box-sizing:border-box;margin:0;padding:0}
html,body{width:1200px;height:2524px;overflow:hidden;background:var(--white)}
body{font-family:"Open Sans",Arial,sans-serif;color:var(--ink);position:relative}
.abs{position:absolute}

/* header */
.site-header{position:absolute;left:0;top:0;width:1200px;height:112px;background:var(--white);border-bottom:1px solid var(--line)}
.brand{position:absolute;left:100px;top:34px;display:flex;align-items:center;gap:12px}
.brand-dot{width:34px;height:34px;border-radius:50%;background:var(--green)}
.brand-name{font-family:"Raleway",sans-serif;font-weight:600;font-size:17px;color:var(--ink)}
.main-nav{position:absolute;right:100px;top:46px;display:flex;gap:36px;font-family:"Raleway",sans-serif;font-size:13px;font-weight:600;letter-spacing:.5px;color:#555}
.main-nav a{color:inherit;text-decoration:none}
.main-nav .active{color:var(--green)}

/* hero */
.hero{position:absolute;left:0;top:112px;width:1200px;height:548px;background:radial-gradient(ellipse at 70% 40%,#6a6e70 0%,#3d4042 45%,#1f2123 100%)}
.hero-title{position:absolute;left:0;width:1200px;top:214px;text-align:center;font-family:"Raleway",sans-serif;font-weight:400;color:var(--white);font-size:54px;letter-spacing:1px}
.hero-sub{position:absolute;left:0;width:1200px;top:286px;text-align:center;font-family:"Raleway",sans-serif;color:var(--white);font-size:34px;letter-spacing:1px}
.hero-dots{position:absolute;left:580px;top:456px;display:flex;gap:12px}
.hero-dots span{width:14px;height:14px;border-radius:50%;background:rgba(255,255,255,.5)}
.hero-dots span.on{background:var(--white)}
.hero-bar{position:absolute;left:0;bottom:0;width:1200px;height:6px;background:var(--green)}

/* section titles */
.section-title{position:absolute;left:0;width:1200px;text-align:center;font-family:"Raleway",sans-serif;font-weight:500;color:var(--green);font-size:32px;letter-spacing:1px}
.title-rule{position:absolute;left:560px;width:80px;height:2px;background:var(--green)}

/* welcome */
.welcome-text{position:absolute;left:150px;width:900px;top:770px;text-align:center;font-size:13px;line-height:24px;color:var(--muted)}
.btn{position:absolute;height:36px;line-height:34px;font-size:12px;font-weight:600;text-align:center;letter-spacing:.5px;border-radius:2px}
.btn-primary{left:478px;top:846px;width:118px;background:var(--blue);color:var(--white);border:1px solid var(--blue)}
.btn-outline{left:612px;top:846px;width:110px;color:var(--green);border:1px solid var(--green)}
.divider{position:absolute;left:0;top:940px;width:1200px;height:1px;background:var(--line)}

/* services */
.services{position:absolute;left:0;top:1060px;width:1200px;height:480px;display:grid;grid-template-columns:repeat(3,400px);grid-template-rows:repeat(2,240px)}
.service{position:relative;padding:30px 32px;color:var(--white);background:linear-gradient(135deg,#a9a9a9,#8e8e8e)}
.service.featured{background:linear-gradient(135deg,var(--green),var(--green-dark))}
.service.row2{background:linear-gradient(135deg,#8f8f8f,#6e6e6e)}
.service svg{width:24px;height:24px;display:block;margin-bottom:10px}
.service h3{font-family:"Raleway",sans-serif;font-weight:500;font-size:20px;margin-bottom:14px}
.service p{font-size:12px;line-height:20px;color:rgba(255,255,255,.75);width:250px}

/* blog */
.eyebrow{position:absolute;left:0;width:1200px;top:1560px;text-align:center;font-size:13px;letter-spacing:2px;color:var(--muted)}
.post{position:absolute;top:1700px;width:300px}
.post-thumb{width:300px;height:208px;background:linear-gradient(135deg,#dfe8f2,#7d97b8)}
.post h4{margin-top:22px;font-size:13px;font-weight:600;color:var(--blue)}
.post p{margin-top:8px;font-size:12px;line-height:19px;color:var(--muted)}
.post time{display:flex;align-items:center;gap:8px;margin-top:10px;font-size:12px;color:var(--muted)}

/* contact */
.contact{position:absolute;left:0;top:2060px;width:1200px;height:388px;background:radial-gradient(ellipse at 50% 40%,#2d2d2d,var(--dark) 70%)}
.contact-title{position:absolute;left:0;width:1200px;top:40px;text-align:center;font-family:"Raleway",sans-serif;color:var(--white);font-size:30px;letter-spacing:1px}
.field{position:absolute;left:192px;width:368px;background:var(--white);border:1px solid #ccc;font-size:12px;color:#555;padding:8px 10px}
.info{position:absolute;left:600px;display:flex;align-items:flex-start;gap:12px;font-size:13px;color:#ddd;line-height:20px}
.info svg{flex:none;margin-top:3px}
.send{position:absolute;left:584px;top:2314px;width:90px;height:36px;line-height:34px;text-align:center;border:1px solid var(--white);color:var(--white);font-size:12px;font-weight:600;letter-spacing:1px}
.partner{position:absolute;left:700px;top:2318px;display:flex;align-items:center;gap:10px;font-family:"Open Sans",sans-serif;font-weight:600;font-size:26px;color:var(--white)}
.partner i{width:18px;height:18px;background:var(--white);display:block}

/* footer */
.site-footer{position:absolute;left:0;top:2448px;width:1200px;height:76px;background:var(--darker)}
.copyright{position:absolute;left:100px;top:28px;font-size:12px;color:#888}
.socials{position:absolute;left:888px;top:26px;display:flex;gap:14px}
.socials span{width:20px;height:20px;border-radius:3px;background:#777}
.to-top{position:absolute;right:24px;top:24px}
</style>
</head>
<body>

<header class="site-header">
  <div class="brand"><span class="brand-dot"></span><span class="brand-name">Verbalis Translation</span></div>
  <nav class="main-nav">
    <a class="active">HOME</a><a>ABOUT US</a><a>PRODUCTS &amp; SERVICES</a><a>PATENT GUIDANCE</a><a>CONTACT US</a>
  </nav>
</header>

<section class="hero" role="img" aria-label="Photo of a desk with a laptop, documents and coffee">
  <h1 class="hero-title">ON THE OTHER HAND,WE DENOUNCE</h1>
  <p class="hero-sub">ACCUSANTIUM DOLOREMQUE LAUDAN</p>
  <div class="hero-dots"><span class="on"></span><span></span></div>
  <div class="hero-bar"></div>
</section>

<h2 class="section-title" style="top:696px">WELCOME</h2>
<div class="title-rule" style="top:748px"></div>
<p class="welcome-text">Sed ut perspiciatis unde omnis iste natus error sit voluptatem accusantium doloremque laudantium, totam rem aperiam, eaque ipsa quae ab illo inventore veritatis et quasi architecto beatae vitae dicta sunt explicabo nemo enim ipsam voluptatem.</p>
<a class="btn btn-primary">VIEW MORE</a>
<a class="btn btn-outline">READ MORE</a>
<div class="divider"></div>

<h2 class="section-title" style="top:966px">SERVICES</h2>
<div class="title-rule" style="top:1018px"></div>

<section class="services">
  <article class="service featured">
    <svg viewBox="0 0 24 24"><path d="M12 3C8 9 6 12 6 15a6 6 0 0 0 12 0c0-3-2-6-6-12z" fill="#fff"/></svg>
    <h3>Corporate communications</h3>
    <p>Sed ut perspiciatis unde omnis iste natus error sit voluptatem accusantium doloremque.</p>
  </article>
  <article class="service">
    <svg viewBox="0 0 24 24"><rect x="4" y="5" width="10" height="5" rx="1" transform="rotate(-35 9 7.5)" fill="#fff"/><path d="M10 12l9 8" stroke="#fff" stroke-width="3"/></svg>
    <h3>Legal translations</h3>
    <p>Sed ut perspiciatis unde omnis iste natus error sit voluptatem accusantium doloremque.</p>
  </article>
  <article class="service">
    <svg viewBox="0 0 24 24"><path d="M2 12a10 8 0 0 1 20 0z" fill="#fff"/><path d="M12 12v7a2 2 0 0 1-4 0" stroke="#fff" stroke-width="2" fill="none"/></svg>
    <h3>Financial translations</h3>
    <p>Sed ut perspiciatis unde omnis iste natus error sit voluptatem accusantium doloremque.</p>
  </article>
  <article class="service row2">
    <svg viewBox="0 0 24 24"><path d="M9 3h6v6h6v6h-6v6H9v-6H3V9h6z" fill="#fff"/></svg>
    <h3>Healthcare translations</h3>
    <p>Sed ut perspiciatis unde omnis iste natus error sit voluptatem accusantium doloremque.</p>
  </article>
  <article class="service row2">
    <svg viewBox="0 0 24 24"><path d="M3 20h18M5 18v-6h3v6M10 18V8h3v10M15 18V4h3v14" stroke="#fff" stroke-width="2" fill="none"/></svg>
    <h3>Financial translations</h3>
    <p>Sed ut perspiciatis unde omnis iste natus error sit voluptatem accusantium doloremque.</p>
  </article>
  <article class="service row2">
    <svg viewBox="0 0 24 24"><path d="M2 6h8l2 2h10v12H2z" fill="#fff"/></svg>
    <h3>Audit translations</h3>
    <p>Sed ut perspiciatis unde omnis iste natus error sit voluptatem accusantium doloremque.</p>
  </article>
</section>

<p class="eyebrow">RECENT POSTS</p>
<h2 class="section-title" style="top:1606px">FROM OUR BLOG</h2>

<article class="post" style="left:100px">
  <div class="post-thumb" role="img" aria-label="Photo of business people shaking hands"></div>
  <h4>Nam libero tempore</h4>
  <p>At vero eos et accusamus et iusto odio dignissimos ducimus qui blanditiis praesentium.</p>
  <time><svg width="12" height="12" viewBox="0 0 12 12"><rect x="1" y="2" width="10" height="9" fill="none" stroke="#1f3fa8"/><path d="M1 5h10" stroke="#1f3fa8"/></svg>19 Sep 2015</time>
</article>
<article class="post" style="left:450px">
  <div class="post-thumb" role="img" aria-label="Photo of a person working on a tablet at a laptop" style="background:linear-gradient(135deg,#f2f5f8,#a9bfd6)"></div>
  <h4>Nam libero tempore</h4>
  <p>At vero eos et accusamus et iusto odio dignissimos ducimus qui blanditiis praesentium.</p>
  <time><svg width="12" height="12" viewBox="0 0 12 12"><rect x="1" y="2" width="10" height="9" fill="none" stroke="#1f3fa8"/><path d="M1 5h10" stroke="#1f3fa8"/></svg>19 Sep 2015</time>
</article>
<article class="post" style="left:800px">
  <div class="post-thumb" role="img" aria-label="Photo of a calculator on financial papers" style="background:linear-gradient(135deg,#c9d6e4,#4e6a8c)"></div>
  <h4>Nam libero tempore</h4>
  <p>At vero eos et accusamus et iusto odio dignissimos ducimus qui blanditiis praesentium.</p>
  <time><svg width="12" height="12" viewBox="0 0 12 12"><rect x="1" y="2" width="10" height="9" fill="none" stroke="#1f3fa8"/><path d="M1 5h10" stroke="#1f3fa8"/></svg>19 Sep 2015</time>
</article>

<section class="contact">
  <h2 class="contact-title">CONTACT US NOW !</h2>
</section>
<div class="field" style="top:2186px;height:32px">Name :</div>
<div class="field" style="top:2244px;height:32px">Email :</div>
<div class="field" style="top:2302px;height:118px">Message :</div>

<div class="info" style="top:2180px;width:300px">
  <svg width="14" height="14" viewBox="0 0 14 14"><circle cx="7" cy="7" r="6" fill="none" stroke="#fff"/><circle cx="7" cy="7" r="2" fill="#fff"/></svg>
  <span>On the other hand, we denounce with righteous indignation and dislike men</span>
</div>
<div class="info" style="top:2244px">
  <svg width="14" height="12" viewBox="0 0 14 12"><rect x="1" y="1" width="12" height="10" fill="none" stroke="#fff"/><path d="M1 1l6 5 6-5" fill="none" stroke="#fff"/></svg>
  <span>info@verbalistranslation.example</span>
</div>
<div class="info" style="top:2272px">
  <svg width="14" height="14" viewBox="0 0 14 14"><path d="M3 1l3 3-2 2c1 2 2 3 4 4l2-2 3 3-2 2C6 13 1 8 1 3z" fill="#fff"/></svg>
  <span>(210) 404 7781</span>
</div>
<div class="send">SEND</div>
<div class="partner"><i></i>trobanex</div>

<footer class="site-footer">
  <p class="copyright">© 2015 Verbalis Translation. All rights reserved.</p>
  <div class="socials"><span></span><span></span><span></span><span></span><span></span><span></span><span></span></div>
  <svg class="to-top" width="24" height="24" viewBox="0 0 24 24"><path d="M6 15l6-6 6 6" fill="none" stroke="#888" stroke-width="2"/></svg>
</footer>

</body>
</html>
```